Kestrel Signs Facebook Banner Design

Design a facebook banner for a sign company. I would like to have a modern approach to it.

Product Offering:
Signs
Banners
Decals
Commercial Wraps

```html
<!DOCTYPE html>
<html lang="en">
<head>
<meta charset="utf-8">
<title>Kestrel Signs – Facebook Banner</title>
<link href="https://fonts.googleapis.com/css2?family=Poppins:ital,wght@0,400;0,500;0,700;0,800;1,400;1,700&family=Bebas+Neue&display=swap" rel="stylesheet">
<style>
  :root {
    --red: #d71f27;
    --ink: #1d1d1f;
    --ink-soft: #2e2e31;
    --paper: #f1f1f1;
    --paper-shade: #dcdcdc;
    --white: #ffffff;
  }
  * { margin: 0; padding: 0; box-sizing: border-box; }
  html, body { width: 1200px; height: 457px; overflow: hidden; background: var(--paper); }
  .banner {
    position: relative;
    width: 1200px;
    height: 457px;
    overflow: hidden;
    font-family: "Poppins", sans-serif;
    color: var(--ink);
  }
  .paper-texture {
    position: absolute; inset: 0;
    background: radial-gradient(ellipse at 30% 40%, var(--white) 0%, var(--paper) 55%, var(--paper-shade) 100%);
  }
  .arc { position: absolute; left: 0; top: 0; }

  /* brand */
  .brand {
    position: absolute; left: 37px; top: 34px;
    font-weight: 800; font-size: 20px; line-height: 21px;
    color: var(--red); text-transform: uppercase; letter-spacing: 0.5px;
  }
  .brand span { display: block; padding-left: 36px; }

  /* contact */
  .contact-button {
    position: absolute; left: 37px; top: 198px;
    width: 161px; height: 36px; display: flex;
    border-radius: 5px; overflow: hidden;
  }
  .contact-button .label {
    flex: 1; background: var(--red); color: var(--white);
    font-weight: 700; font-size: 15px; line-height: 36px; padding-left: 11px;
  }
  .contact-button .arrow {
    width: 30px; background: var(--ink-soft);
    display: flex; align-items: center; justify-content: center;
  }
  .call-label { position: absolute; left: 37px; top: 239px; font-style: italic; font-size: 12.5px; }
  .call-number { position: absolute; left: 36px; top: 256px; font-weight: 700; font-size: 20.5px; color: var(--red); letter-spacing: -0.2px; }
  .call-web { position: absolute; left: 37px; top: 285px; font-size: 11.5px; letter-spacing: 1.3px; }

  /* services */
  .services { position: absolute; right: 37px; top: 36px; text-align: right; }
  .services h2 { font-style: italic; font-weight: 700; font-size: 24px; color: var(--red); line-height: 30px; margin-bottom: 6px; }
  .services ul { list-style: none; }
  .services li { font-size: 16px; line-height: 18px; margin-bottom: 11px; position: relative; padding-right: 14px; }
  .services li::after {
    content: ""; position: absolute; right: 1px; top: 5px;
    width: 6px; height: 6px; border-left: 2.5px solid var(--red); border-bottom: 2.5px solid var(--red);
    transform: rotate(45deg);
  }

  /* social */
  .social-rule { position: absolute; left: 1162px; top: 282px; width: 1px; height: 137px; background: var(--ink); }
  .social { position: absolute; left: 1134px; top: 306px; list-style: none; }
  .social li { width: 19px; height: 19px; border-radius: 50%; background: var(--red); margin-bottom: 3px; }

  /* headline */
  .headline {
    position: absolute; left: 450px; top: 140px; width: 400px;
    text-align: center; font-family: "Bebas Neue", sans-serif; line-height: 1;
  }
  .headline .intro { display: block; font-size: 30px; color: var(--ink); letter-spacing: 2px; }
  .headline .intro em { font-style: normal; color: var(--red); }
  .headline .design { display: block; font-size: 100px; color: var(--ink); margin-top: 4px; }
  .headline .printing { display: block; font-size: 100px; color: var(--red); margin-top: -8px; }
  .headline .experts { display: block; font-family: "Poppins", sans-serif; font-weight: 500; font-size: 24px; letter-spacing: 12px; color: var(--ink); margin-top: 6px; padding-left: 12px; }
</style>
</head>
<body>
<div class="banner">
  <div class="paper-texture" role="img" aria-label="Crumpled white paper texture with soft grey halftone dots"></div>

  <svg class="arc" width="1200" height="457" viewBox="0 0 1200 457" aria-hidden="true">
    <path d="M209 457 A457 457 0 0 1 1123 457 L1014 457 A348 348 0 0 0 318 457 Z" fill="var(--red)"/>
  </svg>

  <div class="brand">Kestrel<span>Signs</span></div>

  <div class="contact-button">
    <div class="label">CONTACT US</div>
    <div class="arrow">
      <svg width="12" height="14" viewBox="0 0 12 14"><path d="M6 1 V12 M1.5 8 L6 12.5 L10.5 8" stroke="#fff" stroke-width="1.8" fill="none" stroke-linecap="round"/></svg>
    </div>
  </div>
  <p class="call-label">Call us Now:</p>
  <p class="call-number">+1 604-555-0187</p>
  <p class="call-web">www.kestrelsigns.ca</p>

  <section class="services">
    <h2>Our Services</h2>
    <ul>
      <li>Signs</li>
      <li>Banners</li>
      <li>Decals</li>
      <li>Commercial<br>Wraps</li>
    </ul>
  </section>

  <div class="social-rule"></div>
  <ul class="social" aria-label="Social links">
    <li></li><li></li><li></li><li></li><li></li>
  </ul>

  <h1 class="headline">
    <span class="intro">We are <em>top sign</em></span>
    <span class="design">DESIGN</span>
    <span class="printing">PRINTING</span>
    <span class="experts">EXPERTS</span>
  </h1>
</div>
</body>
</html>
```